Teskar Business Cards

We need new Business Cards for our startup. It just launched.It is working in the high-end it-market. Specifically in the cloud area. We are a hybrid cloud company. The company logo is attached. We are a Swiss based company. Information visible on the card is: 1. Logo 2. Company Name: Teskar AG 3. Subtitle: Hybrid Clouds. 3. Name: Lukas Brenner 4. Adress: Holderweg 12a, 8462 Ostlingen, Varland 5. Email: lukas@teskar.example. 6. Mobile: +41 79 304 62 18. It should be a grey/white design. Similar to the attached logo. It should have class, high-quality but not too much color and no gold used.

I forgot to add my Position. Please use Founder / CEO. thanks lukas

```html
<!DOCTYPE html>
<html lang="en">
<head>
<meta charset="utf-8">
<title>Teskar AG – Business Card Options</title>
<link href="https://fonts.googleapis.com/css2?family=Arimo:wght@400;700&display=swap" rel="stylesheet">
<style>
:root{
  --paper:#ffffff;
  --ink:#4a4a4a;
  --ink-soft:#7d7d7d;
  --ink-light:#a8a8a8;
  --rule:#5a5a5a;
  --tint:#d6d6d6;
  --faint:#f1f1f1;
  --shadow:rgba(0,0,0,.28);
}
*{margin:0;padding:0;box-sizing:border-box}
html,body{width:1200px;height:900px;overflow:hidden;background:var(--paper)}
body{position:relative;font-family:"Arimo",Arial,sans-serif;color:var(--ink)}
.card{position:absolute;background:var(--paper);box-shadow:2px 3px 7px var(--shadow);overflow:hidden}
.card.landscape{width:275px;height:155px}
.card.portrait{width:156px;height:276px}
.card > *{position:absolute}
.centered{left:0;right:0;text-align:center}
.logo{display:flex;align-items:center;gap:7px;font-size:13px;letter-spacing:4px;color:var(--ink-soft);white-space:nowrap}
.logo::before{content:"";width:9px;height:9px;border-radius:50%;background:var(--ink-light)}
.centered.logo{justify-content:center}
.company{font-size:11.5px;font-weight:700;letter-spacing:.6px;color:var(--ink-soft);white-space:nowrap}
.company .tag{display:block;font-size:5.5px;font-weight:400;letter-spacing:1.3px;margin-top:1px}
.right{text-align:right}
.name{font-size:10px;font-weight:700;color:var(--ink);white-space:nowrap}
.name.large{font-size:12px}
.name.pale{color:var(--ink-soft)}
.details{font-size:6px;line-height:8px;color:var(--ink);white-space:nowrap}
.details.pale{color:var(--ink-soft)}
.rule{background:var(--rule)}
.faint-word{font-size:20px;letter-spacing:4px;color:var(--faint);writing-mode:vertical-rl;white-space:nowrap}
svg.accent{left:0;top:0}
</style>
</head>
<body>

<!-- column 1 -->
<section class="card landscape" style="left:95px;top:10px">
  <p class="name" style="left:10px;top:7px">LUKAS BRENNER</p>
  <p class="logo" style="left:150px;top:18px">TESKAR</p>
  <p class="company" style="left:10px;top:72px">TESKAR AG 3<span class="tag">HYBRID CLOUDS</span></p>
  <p class="details" style="left:10px;top:108px">Holderweg 12a<br>8462 Ostlingen, Varland</p>
  <p class="details" style="left:10px;top:132px">Cell: +41 79 304 62 18<br>Email: lukas@teskar.example</p>
</section>

<section class="card landscape" style="left:95px;top:193px">
  <p class="name" style="left:10px;top:8px">LUKAS BRENNER</p>
  <p class="company" style="left:175px;top:43px">TESKAR AG 3<span class="tag">HYBRID CLOUDS</span></p>
  <p class="details" style="left:175px;top:73px">Holderweg 12a<br>8462 Ostlingen, Varland</p>
  <p class="details" style="left:175px;top:98px">Cell: +41 79 304 62 18<br>Email: lukas@teskar.example</p>
  <p class="logo" style="left:12px;top:125px">TESKAR</p>
  <span class="rule" style="left:252px;top:143px;width:11px;height:11px"></span>
</section>

<section class="card landscape" style="left:95px;top:378px">
  <p class="name large" style="right:10px;top:8px">LUKAS BRENNER</p>
  <p class="logo" style="left:12px;top:32px">TESKAR</p>
  <p class="details" style="left:10px;top:100px">Holderweg 12a<br>8462 Ostlingen, Varland</p>
  <span class="rule" style="left:10px;top:124px;width:72px;height:1px"></span>
  <p class="details" style="left:10px;top:135px">Cell: +41 79 304 62 18<br>Email: lukas@teskar.example</p>
  <p class="company" style="left:178px;top:103px">TESKAR AG 3<span class="tag">HYBRID CLOUDS</span></p>
</section>

<section class="card landscape" style="left:95px;top:556px">
  <p class="logo" style="left:150px;top:17px">TESKAR</p>
  <p class="company right" style="right:10px;top:47px">TESKAR AG 3<span class="tag">HYBRID CLOUDS</span></p>
  <p class="name large" style="left:10px;top:72px">LUKAS BRENNER</p>
  <p class="details" style="left:10px;top:97px">Holderweg 12a<br>8462 Ostlingen, Varland</p>
  <span class="rule" style="left:10px;top:118px;width:75px;height:1px"></span>
  <p class="details" style="left:10px;top:134px">Cell: +41 79 304 62 18<br>Email: lukas@teskar.example</p>
</section>

<section class="card landscape" style="left:95px;top:735px">
  <p class="logo" style="left:12px;top:17px">TESKAR</p>
  <p class="company right" style="right:8px;top:18px">TESKAR AG 3<span class="tag">HYBRID CLOUDS</span></p>
  <p class="name large pale" style="left:18px;top:87px">LUKAS BRENNER</p>
  <span class="rule" style="left:18px;top:110px;width:240px;height:1px"></span>
  <p class="details" style="left:22px;top:121px">Cell: +41 79 304 62 18<br>Email: lukas@teskar.example</p>
  <p class="details" style="left:178px;top:121px">Holderweg 12a<br>8462 Ostlingen, Varland</p>
</section>

<!-- column 2 -->
<section class="card landscape" style="left:395px;top:10px">
  <p class="logo" style="left:12px;top:16px">TESKAR</p>
  <p class="company centered" style="top:65px">TESKAR AG 3<span class="tag">HYBRID CLOUDS</span></p>
  <p class="name" style="left:8px;top:115px">LUKAS BRENNER</p>
  <span class="rule" style="left:130px;top:112px;width:3px;height:36px"></span>
  <p class="details" style="left:178px;top:110px">Holderweg 12a<br>8462 Ostlingen, Varland</p>
  <p class="details" style="left:178px;top:131px">Cell: +41 79 304 62 18<br>Email: lukas@teskar.example</p>
</section>

<section class="card landscape" style="left:390px;top:192px">
  <p class="logo" style="left:72px;top:52px">TESKAR</p>
  <p class="details" style="left:180px;top:106px">Holderweg 12a<br>8462 Ostlingen, Varland</p>
  <p class="details" style="left:180px;top:128px">Cell: +41 79 304 62 18<br>Email: lukas@teskar.example</p>
  <p class="name" style="left:8px;top:130px">LUKAS BRENNER</p>
  <span style="left:0;bottom:0;width:275px;height:5px;background:var(--ink-light)"></span>
</section>

<section class="card landscape" style="left:390px;top:378px">
  <p class="company" style="left:10px;top:12px">TESKAR AG 3<span class="tag" style="padding-left:10px">HYBRID CLOUDS</span></p>
  <p class="logo" style="left:10px;top:72px">TESKAR</p>
  <span style="left:152px;top:50px;width:1px;height:50px;background:var(--tint)"></span>
  <p class="name" style="left:183px;top:50px">LUKAS BRENNER</p>
  <p class="details" style="left:183px;top:69px">Holderweg 12a<br>8462 Ostlingen, Varland</p>
  <p class="details" style="left:183px;top:91px">Cell: +41 79 304 62 18<br>Email: lukas@teskar.example</p>
</section>

<section class="card landscape" style="left:390px;top:551px">
  <p class="company" style="left:8px;top:15px">TESKAR AG 3<span class="tag" style="padding-left:10px">HYBRID CLOUDS</span></p>
  <p class="logo" style="left:128px;top:14px">TESKAR</p>
  <p class="details" style="left:5px;top:75px">Holderweg 12a<br>8462 Ostlingen, Varland</p>
  <p class="details" style="left:5px;top:97px">Cell: +41 79 304 62 18<br>Email: lukas@teskar.example</p>
  <span class="rule" style="left:5px;top:121px;width:98px;height:3px"></span>
  <p class="name" style="left:5px;top:132px">LUKAS BRENNER</p>
</section>

<section class="card landscape" style="left:390px;top:735px">
  <svg class="accent" width="275" height="155" viewBox="0 0 275 155" aria-hidden="true">
    <polygon points="275,0 100,155 150,155" fill="#e6e6e6"/>
    <polygon points="275,0 150,155 185,155" fill="#cfcfcf"/>
    <polygon points="275,0 185,155 210,155" fill="#e0e0e0"/>
  </svg>
  <p class="logo" style="left:10px;top:16px">TESKAR</p>
  <p class="name" style="right:10px;top:5px">LUKAS BRENNER</p>
  <p class="company" style="left:8px;top:58px">TESKAR AG 3<span class="tag" style="padding-left:10px">HYBRID CLOUDS</span></p>
  <p class="details" style="left:5px;top:105px">Phone: (555) 210-4417<br>Fax: (555) 210-4490</p>
  <p class="details" style="left:5px;top:128px">Cell: (555) 382-1906<br>Email: j.weller@corvanta.example</p>
</section>

<!-- column 3 -->
<section class="card portrait" style="left:694px;top:10px">
  <p class="logo" style="left:10px;top:29px">TESKAR</p>
  <p class="company centered" style="top:67px">TESKAR AG 3<span class="tag">HYBRID CLOUDS</span></p>
  <p class="name" style="left:8px;top:199px">LUKAS BRENNER</p>
  <p class="details" style="left:8px;top:225px">Holderweg 12a<br>8462 Ostlingen, Varland</p>
  <p class="details" style="left:8px;top:244px">Cell: +41 79 304 62 18<br>Email: lukas@teskar.example</p>
</section>

<section class="card portrait" style="left:694px;top:300px">
  <svg class="accent" width="156" height="276" viewBox="0 0 156 276" aria-hidden="true">
    <polygon points="156,212 62,266 156,266" fill="#9a9a9a"/>
    <polygon points="156,226 68,276 156,276" fill="#5e5e5e"/>
  </svg>
  <p class="logo" style="left:10px;top:18px">TESKAR</p>
  <p class="company" style="left:4px;top:45px">TESKAR AG 3<span class="tag" style="padding-left:11px">HYBRID CLOUDS</span></p>
  <p class="name" style="left:8px;top:150px">LUKAS BRENNER</p>
  <span class="rule" style="left:8px;top:168px;width:48px;height:3px"></span>
  <p class="details" style="left:8px;top:180px">Holderweg 12a<br>8462 Ostlingen, Varland</p>
  <p class="details" style="left:8px;top:203px">Cell: +41 79 304 62 18<br>Email: lukas@teskar.example</p>
</section>

<section class="card portrait" style="left:696px;top:606px">
  <p class="logo" style="left:10px;top:22px">TESKAR</p>
  <p class="company" style="left:8px;top:68px">TESKAR AG 3<span class="tag">HYBRID CLOUDS</span></p>
  <span class="rule" style="left:151px;top:25px;width:3px;height:226px"></span>
  <p class="name large" style="left:10px;top:195px">LUKAS BRENNER</p>
  <p class="details" style="left:10px;top:224px">Holderweg 12a<br>8462 Ostlingen, Varland</p>
  <p class="details" style="left:10px;top:247px">Cell: +41 79 304 62 18<br>Email: lukas@teskar.example</p>
</section>

<!-- column 4 -->
<section class="card portrait" style="left:890px;top:10px">
  <p class="company centered" style="top:65px">TESKAR AG 3<span class="tag">HYBRID CLOUDS</span></p>
  <p class="logo centered" style="top:132px">TESKAR</p>
  <span style="left:12px;top:177px;width:25px;height:5px;background:var(--ink-light)"></span>
  <p class="name large pale" style="left:10px;top:202px">LUKAS BRENNER</p>
  <p class="details pale" style="left:10px;top:231px">Holderweg 12a<br>8462 Ostlingen, Varland</p>
  <p class="details pale" style="left:10px;top:255px">Cell: +41 79 304 62 18<br>Email: lukas@teskar.example</p>
</section>

<section class="card portrait" style="left:890px;top:303px">
  <p class="faint-word" style="left:48px;top:36px">CORVANTA</p>
  <p class="name centered" style="top:15px">LUKAS BRENNER</p>
  <p class="company centered" style="top:105px">TESKAR AG 3<span class="tag">HYBRID CLOUDS</span></p>
  <p class="logo centered" style="top:182px">TESKAR</p>
  <p class="details pale" style="left:24px;top:220px">Holderweg 12a<br>8462 Ostlingen, Varland</p>
  <p class="details pale" style="left:24px;top:242px">Cell: +41 79 304 62 18<br>Email: lukas@teskar.example</p>
  <span class="rule" style="left:25px;top:272px;width:128px;height:3px"></span>
</section>

<section class="card portrait" style="left:890px;top:606px">
  <p class="faint-word" style="left:62px;top:45px">TESKAR</p>
  <p class="logo centered" style="top:15px">TESKAR</p>
  <p class="company centered" style="top:72px">TESKAR AG 3<span class="tag">HYBRID CLOUDS</span></p>
  <p class="name large centered" style="top:193px">LUKAS BRENNER</p>
  <p class="details" style="left:24px;top:220px">Holderweg 12a<br>8462 Ostlingen, Varland</p>
  <p class="details" style="left:24px;top:243px">M : +41 79 304 62 18<br>E : lukas@teskar.example</p>
  <span class="rule" style="left:8px;top:265px;width:135px;height:4px"></span>
</section>

</body>
</html>
```